Web Design Project for Industrial Hemp

I'm launching a new company to grow Industrial Hemp and then to set up a manufacturing facility to process the crop each and every year. We require a complete end to end brand and livery suite and we will start with a web presence. We want to appeal to (a) Investors, Employees, Farmers, and consumers so as to engage with all our stakeholders. We want to create a whole new industry that becomes a game changer for environmentally friendly crop production. Hemp is gaining in popularity and credibility across the world!

Target Market(s)

Farmers to produce, Manufacturers who will purchase the raw materials, Investors who will invest in the project, Consumers who will buy Hemp Products

Industry/Entity Type

Industry

Requirements
Must have
• Environmentally Friendly
Carbon Neutral/Positive
Game Changer
Multi-Use Crop
50,000 products can be made from Hemp
Should not have
• Should avoid its relationship with cannabis but not ignore it! When the regulatory bodies acknowledge the benefits of cannabanoids, they will start to legalise the production of cannabis for sale on prescription

```html
<!DOCTYPE html>
<html lang="en">
<head>
<meta charset="utf-8">
<title>Verdant Stalk &amp; Fibre Ltd. — What We Are</title>
<link rel="stylesheet" href="https://fonts.googleapis.com/css2?family=Vollkorn+SC:wght@700;900&family=Crimson+Text:wght@400&display=swap">
<style>
  :root {
    --frame-green: #1f7a4a;
    --frame-green-dark: #10573a;
    --frame-green-light: #3a9a67;
    --parchment: #efe2c8;
    --parchment-dark: #cdb894;
    --parchment-light: #f7eedc;
    --nav-top: #9fbf72;
    --nav-bottom: #e2ead0;
    --ink: #171411;
    --heading-green: #0e6b2e;
    --photo-cool: #6f8fae;
    --photo-warm: #8a7a4c;
  }
  * { margin: 0; padding: 0; box-sizing: border-box; }
  html, body { width: 1200px; height: 900px; overflow: hidden; background: var(--frame-green); }
  .page {
    position: relative;
    width: 1200px; height: 900px;
    background:
      repeating-linear-gradient(90deg, rgba(255,255,255,0.03) 0 2px, transparent 2px 5px),
      repeating-linear-gradient(0deg, rgba(0,0,0,0.04) 0 2px, transparent 2px 6px),
      radial-gradient(ellipse at 50% 45%, var(--frame-green-light), var(--frame-green) 55%, var(--frame-green-dark));
    font-family: "Crimson Text", Georgia, serif;
    color: var(--ink);
  }
  .rule-pair {
    position: absolute; left: 0; top: 390px; width: 1200px; height: 14px;
    border-top: 2px solid rgba(0,0,0,0.35);
    border-bottom: 2px solid rgba(0,0,0,0.35);
  }
  .hero {
    position: absolute; left: 28px; top: 38px; width: 1145px; height: 337px;
    border: 4px solid #f3f1e6;
    box-shadow: 0 2px 8px rgba(0,0,0,0.45);
    background: linear-gradient(160deg, var(--photo-cool), var(--photo-warm));
  }
  .brand {
    position: absolute; left: 36px; top: 32px;
    font-family: "Vollkorn SC", Georgia, serif; font-weight: 900;
    font-size: 51px; letter-spacing: 0.5px; color: var(--ink);
    text-shadow: 0 0 3px #f4f0d8, 0 0 3px #f4f0d8, 0 0 6px #f4f0d8;
  }
  .content {
    position: absolute; left: 28px; top: 425px; width: 1144px; height: 413px;
    background: linear-gradient(180deg, var(--parchment-dark), var(--parchment) 40%, var(--parchment-light));
    box-shadow: 0 2px 6px rgba(0,0,0,0.4);
  }
  .ribbon { position: absolute; left: 0; top: 0; width: 1200px; height: 470px; pointer-events: none; }
  .section-title {
    position: absolute; left: 140px; top: 350px; width: 935px; text-align: center;
    font-family: "Vollkorn SC", Georgia, serif; font-weight: 900;
    font-size: 57px; color: var(--heading-green);
    -webkit-text-stroke: 1.5px #05200f;
    text-shadow: 0 0 2px #fff;
  }
  .nav {
    position: absolute; left: 36px; top: 440px; width: 311px; height: 390px;
    border-radius: 10px;
    background: linear-gradient(180deg, var(--nav-top), var(--nav-bottom));
    box-shadow: 3px 4px 6px rgba(0,0,0,0.45);
    list-style: none; padding: 40px 0 0 62px;
  }
  .nav li {
    font-family: "Vollkorn SC", Georgia, serif; font-weight: 700;
    font-size: 26px; line-height: 62px; color: var(--ink);
  }
  .intro {
    position: absolute; left: 390px; top: 490px; width: 762px;
    font-size: 25.5px; line-height: 31px;
  }
  .intro p { text-indent: 42px; }
  .intro strong { font-family: "Vollkorn SC", Georgia, serif; font-weight: 700; font-size: 25px; }
  .footer {
    position: absolute; left: 0; top: 842px; width: 1200px; height: 48px;
    border-top: 2px solid rgba(0,0,0,0.45);
    border-bottom: 2px solid rgba(0,0,0,0.3);
    background: linear-gradient(180deg, #e8dcc0, var(--parchment-light));
    text-align: center; padding-top: 12px;
    font-family: "Vollkorn SC", Georgia, serif; font-weight: 700; font-size: 20px;
    word-spacing: 1px;
  }
  .footer .sep { margin: 0 12px; }
</style>
</head>
<body>
<div class="page">
  <div class="rule-pair"></div>
  <div class="hero" role="img" aria-label="Landscape photograph of autumn hills above a blue bay with a coastal town"></div>
  <div class="brand">Verdant Stalk &amp; Fibre Ltd.</div>

  <div class="content"></div>

  <svg class="ribbon" viewBox="0 0 1200 470" aria-hidden="true">
    <defs>
      <linearGradient id="ribbonFill" x1="0" x2="1" y1="0" y2="0">
        <stop offset="0" stop-color="#f6ecd8"/>
        <stop offset="0.5" stop-color="#efe2c8"/>
        <stop offset="1" stop-color="#b9a381"/>
      </linearGradient>
    </defs>
    <path d="M145,338 Q420,352 600,322 Q780,352 1072,338 Q1040,388 1072,442 Q780,428 600,454 Q420,428 145,442 Q178,390 145,338 Z"
          fill="url(#ribbonFill)" stroke="#120f0a" stroke-width="4"/>
  </svg>
  <h1 class="section-title">What We Are</h1>

  <ul class="nav">
    <li>Home</li>
    <li>Knowledge</li>
    <li>Green</li>
    <li>Farming</li>
    <li>Products</li>
  </ul>

  <div class="intro">
    <p><strong>Verdant Stalk &amp; Fibre Ltd.</strong> is an environmentally sustainable company committed to the manufacturing and growth of Industrial Hemp. This exciting new multi-use crop is a game changer in local and international markets. Etiam sed tortor ac sem pellentesque euismod. Nunc risus. Sed turpis quam, adipiscing nec, dapibus nec, bibendum sed, eros. Quisque nec mi. Mauris in massa.</p>
    <p>Aliquam eu nibh. Praesent molestie lorem ac eros. Aliquam blandit quam. Lorem ipsum dolor sit amet, consectetuer adipiscing elit. Vivamus auctor commodo enim.</p>
  </div>

  <footer class="footer">
    12 Harbour Lane, Glenmore Bay, Ireland<span class="sep">•</span>+353-1-555-0142<span class="sep">•</span>HELLO@VERDANTSTALKFIBRE.COM
  </footer>
</div>
</body>
</html>
```